Estate Agent/Real Estate valuation tool

We need a design for our our new estate agent valuation tool.

The tool allows users to book a valuation of their house/property with the estate agent, after they choose there property they can then complete their details and choose a booking time.

The mock up of the design we want is attached to this project.(Main Screen)

This also needs to be responsive so the design is easy to use on a mobile device.

Target Market(s)

Keystone Estates

Industry/Entity Type

Real Estate Agent

Number of Pages Required

1 page

Requirements
Must have
• Section 2 and 3 greyed out when user is on step 1
• Section 1 and 3 greyed out when user is on step 2
• Section 1 and 2 greyed out when the user is on step 3
• *** Design must be shown for mobile/ipad and desktop
Nice to have
• Clean and Simple
Should not have
• Dark colours

```html
<!DOCTYPE html>
<html lang="en">
<head>
<meta charset="utf-8">
<title>Keystone Estates – Book Your Valuation Online</title>
<link rel="stylesheet" href="https://fonts.googleapis.com/css2?family=Cinzel:wght@400;500&family=Raleway:wght@400;500&display=swap">
<style>
  :root {
    --sky-top: #f7f8fb;
    --sky-mid: #e7ebf3;
    --sky-low: #dfe5ee;
    --brand-ink: #1f2a3a;
    --brand-blue: #2aa9e8;
    --headline: #5f86c7;
    --pink: #ef3e67;
    --pink-line: #e6315d;
    --lilac: #d3c6e9;
    --lilac-line: #9b82cc;
    --mint: #b6e3c8;
    --mint-line: #2bb35b;
    --panel-active: rgba(255,255,255,0.9);
    --panel-muted: rgba(246,246,246,0.82);
    --field-line: #cfcfcf;
    --field-muted: #e2e2e2;
    --text-muted: #b0b0b0;
    --text-dark: #2f2f2f;
    --btn-dark: #2f2f2f;
    --btn-muted: #bdbdbd;
    --chip-bg: #bfe6cd;
    --chip-line: #a6dab9;
    --chip-text: #8fc7a3;
    --chip-selected: #b7b7b7;
    --footer: #29b5f0;
    --white: #ffffff;
    --social-1: #3c5a99;
    --social-2: #1da1f2;
    --social-3: #1b86bf;
    --social-4: #d44638;
  }
  * { box-sizing: border-box; margin: 0; padding: 0; }
  html, body { width: 1200px; height: 562px; overflow: hidden; }
  body {
    position: relative;
    font-family: "Raleway", sans-serif;
    background: var(--sky-top);
  }
  .backdrop {
    position: absolute; inset: 0 0 42px 0;
    background: linear-gradient(180deg, var(--sky-top) 0%, var(--sky-top) 45%, var(--sky-mid) 62%, var(--sky-low) 80%, var(--sky-mid) 100%);
  }
  .brand {
    position: absolute; top: 36px; left: 0; width: 1200px;
    display: flex; justify-content: center; align-items: center; gap: 12px;
  }
  .brand-square { width: 22px; height: 22px; background: var(--brand-blue); }
  .brand-name {
    font-family: "Cinzel", serif; font-weight: 400; font-size: 36px;
    color: var(--brand-ink); letter-spacing: 1px; line-height: 1;
  }
  .headline {
    position: absolute; top: 106px; left: 0; width: 1200px; text-align: center;
    font-family: "Cinzel", serif; font-weight: 400; font-size: 24px;
    color: var(--headline); letter-spacing: 1px;
  }
  .step {
    position: absolute; top: 160px; width: 270px; height: 310px;
    background: var(--panel-muted);
    box-shadow: 0 1px 4px rgba(0,0,0,0.08);
    border-radius: 3px;
  }
  .step--active { background: var(--panel-active); }
  .step--property { left: 162px; border-bottom: 3px solid var(--pink-line); }
  .step--contact { left: 465px; border-bottom: 3px solid var(--lilac-line); }
  .step--time { left: 770px; border-bottom: 3px solid var(--mint-line); }
  .step-title {
    height: 38px; line-height: 38px; text-align: center;
    color: var(--white); font-size: 18px; font-weight: 400;
    border-radius: 3px 3px 0 0;
  }
  .step--property .step-title { background: var(--pink); }
  .step--contact .step-title { background: var(--lilac); }
  .step--time .step-title { background: var(--mint); }
  .field {
    position: absolute; left: 15px; width: 238px; height: 32px;
    border: 1px solid var(--field-muted); border-radius: 3px;
    padding-left: 11px; line-height: 30px;
    font-size: 13px; color: var(--text-muted);
    background: rgba(255,255,255,0.35);
  }
  .postcode-row {
    position: absolute; left: 15px; top: 64px; width: 238px; height: 32px; display: flex;
  }
  .postcode-input {
    flex: 1; border: 1px solid #9a9a9a; border-right: none; border-radius: 3px 0 0 3px;
    padding-left: 12px; line-height: 30px; font-size: 13.5px; color: var(--text-dark); background: var(--white);
  }
  .search-btn {
    width: 83px; background: var(--btn-dark); color: var(--white);
    border-radius: 0 3px 3px 0; text-align: center; line-height: 32px; font-size: 14px;
  }
  .proceed {
    position: absolute; left: 64px; top: 252px; width: 141px; height: 32px;
    line-height: 32px; text-align: center; font-size: 15px; color: var(--white);
    border-radius: 2px;
  }
  .proceed--ready { background: var(--btn-dark); }
  .proceed--waiting { background: var(--btn-muted); border: 1px solid #b0b0b0; }
  .day-chips {
    position: absolute; left: 15px; top: 53px; width: 240px; display: flex; justify-content: space-between;
  }
  .day-chip {
    width: 30px; height: 30px; border: 1px solid var(--chip-line); border-radius: 2px;
    background: var(--chip-bg); color: var(--chip-text);
    font-size: 7px; line-height: 8px; text-align: center;
    display: flex; align-items: center; justify-content: center;
  }
  .day-chip--selected { background: var(--chip-selected); border-color: #a8a8a8; color: var(--white); }
  .slot {
    position: absolute; left: 15px; width: 239px; height: 29px; display: flex;
    border: 1px solid var(--field-muted); border-radius: 2px; background: rgba(255,255,255,0.4);
  }
  .slot-date { flex: 1; padding-left: 9px; line-height: 27px; font-size: 13px; color: var(--text-muted); }
  .slot-time {
    width: 53px; background: var(--chip-selected); color: var(--white);
    text-align: center; line-height: 27px; font-size: 13px;
  }
  .confirm {
    position: absolute; left: 60px; top: 266px; width: 141px; height: 32px;
    line-height: 32px; text-align: center; font-size: 15px; color: var(--white);
    background: var(--btn-muted); border: 1px solid #b0b0b0; border-radius: 2px;
  }
  .footer {
    position: absolute; left: 0; bottom: 0; width: 1200px; height: 42px; background: var(--footer);
  }
  .footer-note {
    position: absolute; left: 163px; top: 0; line-height: 42px; font-size: 11.5px; color: var(--white);
  }
  .social { position: absolute; right: 164px; top: 6px; display: flex; gap: 14px; }
  .social-dot { width: 30px; height: 30px; border-radius: 50%; border: 2px solid #e9f2f7; }
  .social-dot--one { background: var(--social-1); }
  .social-dot--two { background: var(--social-2); }
  .social-dot--three { background: var(--social-3); }
  .social-dot--four { background: var(--social-4); }
</style>
</head>
<body>
  <div class="backdrop" role="img" aria-label="Faint photograph of a waterfront city skyline"></div>

  <header class="brand">
    <span class="brand-square"></span>
    <span class="brand-name">Keystone Estates</span>
  </header>
  <h1 class="headline">Book Your Valuation Online</h1>

  <section class="step step--property step--active">
    <h2 class="step-title">PROPERTY DETAILS</h2>
    <div class="postcode-row">
      <div class="postcode-input">Postcode</div>
      <div class="search-btn">Search</div>
    </div>
    <div class="field" style="top:109px">Street</div>
    <div class="field" style="top:154px">City</div>
    <div class="field" style="top:199px">Country</div>
    <div class="proceed proceed--ready">Proceed</div>
  </section>

  <section class="step step--contact">
    <h2 class="step-title">YOUR DETAILS</h2>
    <div class="field" style="top:64px">Name</div>
    <div class="field" style="top:109px">Email</div>
    <div class="field" style="top:154px">Number</div>
    <div class="proceed proceed--waiting">Proceed</div>
  </section>

  <section class="step step--time">
    <h2 class="step-title">APPOINTMENT TIME</h2>
    <div class="day-chips">
      <div class="day-chip">Today</div>
      <div class="day-chip day-chip--selected">Tomo-<br>rrow</div>
      <div class="day-chip">Mon<br>30th</div>
      <div class="day-chip">Tue<br>01st</div>
      <div class="day-chip">Wed<br>02st</div>
      <div class="day-chip">Thurs<br>04st</div>
      <div class="day-chip">Fri<br>05tht</div>
    </div>
    <div class="slot" style="top:89px"><span class="slot-date">Sunday 29th November</span><span class="slot-time">08 : 30</span></div>
    <div class="slot" style="top:123px"><span class="slot-date">Sunday 29th November</span><span class="slot-time">10 : 30</span></div>
    <div class="slot" style="top:157px"><span class="slot-date">Sunday 29th November</span><span class="slot-time">12 : 30</span></div>
    <div class="slot" style="top:192px"><span class="slot-date">Sunday 29th November</span><span class="slot-time">14 : 30</span></div>
    <div class="slot" style="top:226px"><span class="slot-date">Sunday 29th November</span><span class="slot-time">16 : 30</span></div>
    <div class="confirm">Confrim Booking</div>
  </section>

  <footer class="footer">
    <p class="footer-note">Harbourline Software Ltd. All rights reserved.</p>
    <div class="social">
      <span class="social-dot social-dot--one"></span>
      <span class="social-dot social-dot--two"></span>
      <span class="social-dot social-dot--three"></span>
      <span class="social-dot social-dot--four"></span>
    </div>
  </footer>
</body>
</html>
```